Business card design for Healthcare Clinic

Need to create an elegant business card design that incorporates a QR code to a specific page on the website

Industry/Entity Type

Healthcare

Contact Information for Business Card

Name, job title, address, phone number, fax number, website

Font styles to use
Serif
Sans Serif

Colors
0054AA
0677BA
7BADD7
CADEEF
E8F1F8
0094D4
00A9DD
6FCCEA
C7EBF8
E9F6FB
6B429C
8869AF
B7A5CE
E3DAEB
F3F0F8

Requirements
Must have
• QR Code on the back side that will link to a specific website page (use place holder for now)
Nice to have
• Maybe try to incorporate the logo design elements (DNA strand) into the design. Please inquire for website if you want to see.

```html
<!DOCTYPE html>
<html lang="en">
<head>
<meta charset="utf-8">
<title>Northfield Sports Recovery Clinic — Business Card</title>
<link href="https://fonts.googleapis.com/css2?family=Cormorant+Garamond:wght@500;600&family=Montserrat:wght@400;500;600&display=swap" rel="stylesheet">
<style>
  :root {
    --backdrop: #bcc9c6;
    --paper: #f6f7f8;
    --navy: #0054aa;
    --ink: #2b3a8c;
    --sky: #00a9dd;
    --sky-light: #6fccea;
    --sky-pale: #c7ebf8;
    --lilac: #b7a5ce;
    --lilac-pale: #e3daeb;
    --text-soft: #5a6aa8;
  }
  * { box-sizing: border-box; margin: 0; padding: 0; }
  html, body { width: 1200px; height: 950px; overflow: hidden; }
  body {
    background: var(--backdrop);
    display: flex;
    align-items: center;
    justify-content: center;
    gap: 40px;
    font-family: "Montserrat", sans-serif;
  }
  .card {
    position: relative;
    width: 540px;
    height: 309px;
    background: var(--paper);
    overflow: hidden;
    box-shadow: 0 18px 40px rgba(40, 60, 60, 0.22);
  }

  /* Back side */
  .card-back .pattern-area {
    position: absolute;
    top: 0; left: 110px; right: 0; height: 120px;
    background: radial-gradient(ellipse at 60% 0%, var(--lilac-pale) 0%, rgba(227,218,235,0.35) 45%, rgba(246,247,248,0) 75%);
  }
  .card-back .brand {
    position: absolute;
    top: 128px; left: 0; right: 0;
    text-align: center;
  }
  .brand-name {
    font-family: "Cormorant Garamond", serif;
    font-weight: 600;
    font-size: 31px;
    color: var(--ink);
    letter-spacing: 0.2px;
  }
  .brand-rule {
    position: absolute;
    left: 60px; right: 60px;
    height: 1px;
    background: var(--sky-light);
  }
  .brand-rule.top { top: 112px; opacity: 0.6; }
  .brand-rule.bottom { top: 264px; }
  .website {
    position: absolute;
    right: 70px; top: 232px;
    font-size: 12px;
    font-weight: 600;
    color: var(--ink);
    letter-spacing: 0.5px;
  }

  /* Front side */
  .card-front .photo {
    position: absolute;
    top: 0; right: 0;
    width: 196px; height: 206px;
    background: linear-gradient(160deg, var(--sky-pale) 0%, #e9e3e6 55%, #d9d4d6 100%);
  }
  .visit-panel {
    position: absolute;
    right: 10px; top: 124px;
    width: 62px; height: 70px;
    background: #ffffff;
    border: 2px solid var(--sky-light);
    display: flex;
    align-items: flex-start;
    justify-content: center;
    padding-top: 4px;
    font-size: 7px;
    font-weight: 600;
    color: var(--ink);
  }
  .front-brand {
    position: absolute;
    top: 60px; left: 34px;
    font-family: "Cormorant Garamond", serif;
    font-weight: 600;
    font-size: 11px;
    color: var(--ink);
  }
  .person-name {
    position: absolute;
    top: 86px; left: 34px;
    font-family: "Cormorant Garamond", serif;
    font-weight: 500;
    font-size: 30px;
    line-height: 30px;
    letter-spacing: 5px;
    color: var(--navy);
  }
  .person-title {
    position: absolute;
    top: 134px; left: 186px;
    font-family: "Cormorant Garamond", serif;
    font-weight: 600;
    font-size: 11px;
    letter-spacing: 0.6px;
    color: var(--ink);
  }
  .address {
    position: absolute;
    top: 172px; left: 34px;
    font-size: 10px;
    line-height: 14px;
    color: var(--text-soft);
  }
  .contact-list {
    position: absolute;
    top: 210px; left: 50px;
    font-size: 9.5px;
    line-height: 15px;
    color: var(--text-soft);
    list-style: none;
  }
  .contact-list li { display: flex; }
  .contact-list .label { width: 62px; letter-spacing: 1px; }
  .contact-list .sep { width: 12px; }
</style>
</head>
<body>

  <section class="card card-back" aria-label="Card back">
    <div class="pattern-area" role="img" aria-label="Soft lilac geometric background pattern"></div>
    <div class="brand-rule top"></div>
    <div class="brand">
      <span class="brand-name">Northfield Sports Recovery Clinic</span>
    </div>
    <p class="website">www.northfieldrecovery.com</p>
    <div class="brand-rule bottom"></div>
  </section>

  <section class="card card-front" aria-label="Card front">
    <div class="photo" role="img" aria-label="Portrait photograph of the clinic founder"></div>
    <div class="visit-panel">visit our site</div>

    <p class="front-brand">Northfield Sports Recovery Clinic</p>
    <h1 class="person-name">MAREN<br>OAKLEY</h1>
    <p class="person-title">CEO &amp; FOUNDER</p>

    <address class="address" style="font-style:normal">
      418 Linden Avenue<br>Albany, NY 12207
    </address>

    <ul class="contact-list">
      <li><span class="label">EMAIL</span><span class="sep">:</span><span>maren@northfieldrecovery.com</span></li>
      <li><span class="label">PHONE</span><span class="sep">:</span><span>+1 (518) 555 0142</span></li>
      <li><span class="label">FAX</span><span class="sep">:</span><span>+1 (518) 555 0143</span></li>
    </ul>
  </section>

</body>
</html>
```